Security Services Business Card

Looking for a clean modern style business card design for a residential and commercial security solutions provider. We install and service the following
security alarm, access control, video surveillance and fire alarm. Attached are the front and back of our current business cards in PSD file format.

Target Market(s)

Security alarm clients in the commercial and residential markets

Industry/Entity Type

Security Service

Contact Information for Business Card

We are open to designers suggestion and or design ideas.

Font styles to use
Serif
Sans Serif

Colors
3276b5
33a6d7
fffefd

Requirements
Must have
• Must have company logo , first and last name , phone number , web and email address, ect....

```html
<!DOCTYPE html>
<html lang="en">
<head>
<meta charset="utf-8">
<title>Brightward Systems – Business Card</title>
<link rel="stylesheet" href="https://fonts.googleapis.com/css2?family=Roboto:wght@400;500;700&family=Montserrat:wght@700&display=swap">
<style>
  :root {
    --backdrop: #9a9a9a;
    --card-white: #f7f7f5;
    --brand-blue: #33a6d7;
    --deep-blue: #2b9bd0;
    --logo-tint: #bfe2f4;
    --ink-light: #fffefd;
  }
  * { box-sizing: border-box; margin: 0; padding: 0; }
  html, body { width: 1200px; height: 982px; overflow: hidden; }
  body {
    background: var(--backdrop);
    font-family: "Roboto", Arial, sans-serif;
    display: flex;
    flex-direction: column;
    align-items: center;
    justify-content: center;
    gap: 60px;
  }
  .card {
    width: 620px;
    height: 354px;
    position: relative;
    overflow: hidden;
    box-shadow: 0 14px 30px rgba(0,0,0,0.25);
  }
  /* Front */
  .card-front { display: flex; background: var(--card-white); }
  .front-brand {
    flex: 0 0 52%;
    display: flex;
    align-items: center;
    justify-content: center;
  }
  .wordmark {
    display: flex;
    align-items: center;
    gap: 10px;
    color: var(--brand-blue);
  }
  .wordmark-dot {
    width: 16px; height: 16px;
    border-radius: 50%;
    background: var(--brand-blue);
    flex: none;
  }
  .wordmark-name {
    font-weight: 700;
    font-size: 34px;
    letter-spacing: 0.5px;
    line-height: 1;
  }
  .front-details {
    flex: 1;
    background: var(--brand-blue);
    color: var(--ink-light);
    padding: 78px 24px 0 30px;
  }
  .person-name {
    font-family: "Montserrat", Arial, sans-serif;
    font-weight: 700;
    font-size: 16px;
    letter-spacing: 0.3px;
  }
  .person-title { font-size: 13.5px; margin-bottom: 14px; }
  .address { font-size: 13.5px; line-height: 1.35; margin-bottom: 6px; }
  .contact-list { list-style: none; font-size: 13.5px; line-height: 1.55; }
  .contact-list li { display: flex; align-items: center; gap: 7px; }
  .contact-list svg { width: 12px; height: 12px; flex: none; fill: var(--ink-light); }
  /* Back */
  .card-back {
    background: var(--deep-blue);
    color: var(--ink-light);
    display: flex;
    flex-direction: column;
    align-items: center;
  }
  .back-wordmark {
    margin-top: 110px;
    display: flex;
    align-items: center;
    gap: 14px;
    color: var(--logo-tint);
  }
  .back-wordmark .wordmark-dot { width: 22px; height: 22px; background: var(--logo-tint); }
  .back-wordmark .wordmark-name { font-size: 54px; }
  .services {
    list-style: none;
    display: flex;
    gap: 14px;
    position: absolute;
    bottom: 44px;
    font-size: 15.5px;
  }
  .services li::before { content: "• "; }
</style>
</head>
<body>
  <section class="card card-front" aria-label="Business card front">
    <div class="front-brand">
      <div class="wordmark">
        <span class="wordmark-dot"></span>
        <span class="wordmark-name">Brightward Systems</span>
      </div>
    </div>
    <div class="front-details">
      <p class="person-name">MARCUS ELLERY</p>
      <p class="person-title">Managing Director</p>
      <p class="address">4810 Harbor Point Suite #212<br>Lakewood, Ohio 44107</p>
      <ul class="contact-list">
        <li><svg viewBox="0 0 24 24" aria-hidden="true"><path d="M6.6 10.8a15 15 0 0 0 6.6 6.6l2.2-2.2a1 1 0 0 1 1-.25 11.4 11.4 0 0 0 3.6.57 1 1 0 0 1 1 1V20a1 1 0 0 1-1 1A17 17 0 0 1 3 4a1 1 0 0 1 1-1h3.5a1 1 0 0 1 1 1c0 1.25.2 2.45.57 3.57a1 1 0 0 1-.25 1z"/></svg>555.014.2290 ext</li>
        <li><svg viewBox="0 0 24 24" aria-hidden="true"><path d="M2 5h20v14H2zm2 2v.5l8 5 8-5V7zm0 2.8V17h16V9.8l-8 5z"/></svg>info@brightwardinfo.com</li>
        <li><svg viewBox="0 0 24 24" aria-hidden="true"><path d="M12 2a10 10 0 1 0 0 20 10 10 0 0 0 0-20zm0 2c.9 0 2.2 1.9 2.7 5H9.3C9.8 5.9 11.1 4 12 4zM4.3 11h3a17 17 0 0 0 0 2h-3a8 8 0 0 1 0-2zm5 0h5.4a15 15 0 0 1 0 2H9.3a15 15 0 0 1 0-2zm7.4 0h3a8 8 0 0 1 0 2h-3a17 17 0 0 0 0-2zM9.3 15h5.4c-.5 3.1-1.8 5-2.7 5s-2.2-1.9-2.7-5z"/></svg>www.brightwardinfo.com</li>
      </ul>
    </div>
  </section>

  <section class="card card-back" aria-label="Business card back">
    <div class="back-wordmark">
      <span class="wordmark-dot"></span>
      <span class="wordmark-name">Brightward Systems</span>
    </div>
    <ul class="services">
      <li>Video Surveillance</li>
      <li>Security Alarm</li>
      <li>Fire Alarm</li>
      <li>Access Control</li>
    </ul>
  </section>
</body>
</html>
```